Vantor Medica Innovative Business Card

Stunning business card. Background will be black. Letters in gold. Modern yet simple design that is attention grabbing. QR code leading to site. Attractive primarily to males ages 30 to 50 but also to females in same age range looking for beauty and mental health products

Target Market(s)

Males in the 30-50 age demographics

Industry/Entity Type

Pharmaceuticals selling erectile dysfunction and mens health medications

Contact Information for Business Card

www.vantormedica.example; (775) BUY-KELO; info@vantormedica.example

Colors
FFC000
F8CF3A
FAE287
FDF2CF
FEFAEE

Requirements
Must have
• Black business card with gold letters.
Nice to have
• perhaps just the logo or the "R" icon by itself on one side
Should not have
• too much content so it does not look busy

```html
<!DOCTYPE html>
<html lang="en">
<head>
<meta charset="utf-8">
<title>Vantor Medica – Business Card</title>
<link href="https://fonts.googleapis.com/css2?family=Montserrat:wght@500;600&display=swap" rel="stylesheet">
<style>
  :root {
    --page-bg: #ffffff;
    --card-white: #ffffff;
    --card-black: #0b0b0b;
    --panel-dark: #1c1c1c;
    --ink: #111111;
    --gold: #f2c12e;
    --gold-deep: #d4a935;
    --card-edge: #e2e2e2;
  }
  * { margin: 0; padding: 0; box-sizing: border-box; }
  html, body {
    width: 1200px;
    height: 1200px;
    overflow: hidden;
    background: var(--page-bg);
    font-family: "Montserrat", Arial, sans-serif;
  }
  .canvas {
    position: relative;
    width: 1200px;
    height: 1200px;
  }
  .card {
    position: absolute;
    left: 299px;
    width: 603px;
    height: 345px;
    border-radius: 26px;
    overflow: hidden;
  }
  .card--front {
    top: 171px;
    background: var(--card-white);
    border: 1px solid var(--card-edge);
  }
  .card--back {
    top: 683px;
    background: var(--card-black);
  }

  /* front side */
  .front__tab {
    position: absolute;
    left: 0;
    top: 105px;
    width: 22px;
    height: 134px;
    background: var(--panel-dark);
    border-radius: 0 4px 4px 0;
  }
  .front__contacts {
    position: absolute;
    left: 58px;
    top: 100px;
    width: 282px;
    list-style: none;
    color: var(--ink);
    font-size: 18.5px;
    font-weight: 500;
    letter-spacing: 0.1px;
    white-space: nowrap;
  }
  .front__contacts li {
    height: 57px;
    line-height: 30px;
  }
  .front__panel {
    position: absolute;
    right: 0;
    top: 105px;
    width: 246px;
    height: 134px;
    background: var(--panel-dark);
    border-radius: 4px 0 0 4px;
    display: flex;
    align-items: center;
    justify-content: center;
    gap: 10px;
  }
  .brand-dot {
    display: block;
    border-radius: 50%;
    background: var(--gold-deep);
  }
  .front__panel .brand-dot { width: 30px; height: 30px; }
  .brand-name {
    color: var(--gold-deep);
    font-weight: 600;
    white-space: nowrap;
  }
  .front__panel .brand-name { font-size: 18px; }

  /* back side */
  .back__brand {
    position: absolute;
    left: 0;
    right: 0;
    top: 110px;
    display: flex;
    align-items: center;
    justify-content: center;
    gap: 18px;
  }
  .back__brand .brand-dot { width: 96px; height: 96px; }
  .back__brand .brand-name { font-size: 30px; }
  .back__url {
    position: absolute;
    right: 16px;
    bottom: 17px;
    color: var(--gold);
    font-size: 19.5px;
    font-weight: 600;
    letter-spacing: 0.3px;
    white-space: nowrap;
  }
</style>
</head>
<body>
  <main class="canvas">
    <section class="card card--front" aria-label="Business card, front">
      <div class="front__tab"></div>
      <ul class="front__contacts">
        <li>www.vantormedica.example</li>
        <li>(775) BUY-KELO</li>
        <li>info@vantormedica.example</li>
      </ul>
      <div class="front__panel">
        <span class="brand-dot"></span>
        <span class="brand-name">Vantor Medica</span>
      </div>
    </section>

    <section class="card card--back" aria-label="Business card, back">
      <div class="back__brand">
        <span class="brand-dot"></span>
        <span class="brand-name">Vantor Medica</span>
      </div>
      <p class="back__url">www.vantormedica.example</p>
    </section>
  </main>
</body>
</html>
```